Juniper Estates - wanted BRILLIANT website design for our new property investing company

We need a website design for our new company based in Bristol, England, UK called "Juniper Estates". We help buy people property who are in financial difficulty or who are needing to sell their property quickly for reasons such as death, divorce/separation, relocation, emigration.

We have a logo being designed incorporating strawberry and property (so red and green). We would like designs to communicate an elegant ,professional, approachable, friendly
fresh clean but also warm appealing appearance
Not too busy
Website consistent with logo and company name i.e. colour scheme

Please use our word document for content as a guide but use professional judgement for minor alterations if you feel they would benefit the site/structure etc

Please ask at any time if not sure

Target Market(s)

Adult british population, those that have a mortgage / loan / own property

Industry/Entity Type

Financial

Font styles to use
Serif
Sans Serif
Decorative

Colors
0692cd
33b7a4
acd036
fbee3e
3176b5
886aae
a6479a
e567a6
eb1f27

Requirements
Must have
• This must not look like a template website we are looking for UNIQUE please!
Nice to have
• Bristol pictures instead of generic, or colourful line drawings/comic drawings of houses/property/keys/happy people.....
Should not have
• An obvious off the shelf template design

```html
<!DOCTYPE html>
<html lang="en">
<head>
<meta charset="utf-8">
<title>Juniper Estates</title>
<link href="https://fonts.googleapis.com/css2?family=Exo:wght@400;600;700&family=Open+Sans:ital,wght@0,400;0,600;1,400&display=swap" rel="stylesheet">
<style>
:root{
  --blue:#2f78c0;
  --blue-dark:#2163a6;
  --teal:#33b7a4;
  --red:#d4124b;
  --green:#5aad24;
  --lime:#8fc43a;
  --ink:#444;
  --muted:#777;
  --line:#e2e2e2;
  --footer:#222;
  --footer-bar:#3b3b3b;
}
*{box-sizing:border-box;margin:0;padding:0}
html,body{width:698px;height:1200px;overflow:hidden;background:#fff}
body{position:relative;font-family:"Open Sans",sans-serif;color:var(--ink);font-size:7px}
.abs{position:absolute}
h2,h3,.nav a,.btn{font-family:"Exo",sans-serif}

/* header */
.topband{left:0;top:0;width:698px;height:71px;background:linear-gradient(#3a86cf,var(--blue))}
.topband::after{content:"";position:absolute;left:0;right:0;bottom:-4px;height:4px;background:var(--blue-dark)}
.brand{left:72px;top:0;width:128px;height:82px;background:#fafafa;box-shadow:0 1px 4px rgba(0,0,0,.3);display:flex;flex-direction:column;align-items:center;justify-content:flex-end;padding-bottom:14px;gap:6px}
.brand-dot{width:22px;height:22px;border-radius:50%;background:var(--red)}
.brand-name{font-family:"Exo",sans-serif;font-weight:600;font-size:13px;color:var(--red)}
.toplinks{left:230px;top:13px;color:#fff;font-size:6.5px;font-family:"Exo",sans-serif;font-weight:600;display:flex;gap:8px}
.pill{top:9px;height:16px;border-radius:8px;background:var(--lime);color:#fff;font-family:"Exo",sans-serif;font-weight:600;font-size:7px;display:flex;align-items:center;gap:4px;padding:0 8px}
.login{left:402px;top:36px;width:228px;height:24px;background:rgba(255,255,255,.2);display:flex;align-items:center;gap:6px;padding:0 9px}
.login span{height:14px;background:#fff;border:1px solid #ccc;width:74px;font-size:6px;color:#888;padding:2px 4px}
.login b{height:13px;width:50px;background:var(--red);color:#fff;font-family:"Exo",sans-serif;font-size:7px;display:flex;align-items:center;justify-content:center}

/* nav */
.nav{left:73px;top:102px;width:555px;height:26px;background:var(--blue);display:flex;border-radius:2px}
.nav a{color:#fff;text-decoration:none;font-weight:600;font-size:7.5px;display:flex;align-items:center;justify-content:center;border-right:1px solid rgba(0,0,0,.18)}
.nav a:last-child{border:0}

/* hero */
.hero{left:73px;top:142px;width:555px;height:183px;background:#ddd;padding:3px}
.hero-photo{left:3px;top:3px;width:404px;height:177px;background:linear-gradient(160deg,#f1e27a 0%,#e9d45c 45%,#7aa35a 70%,#5d8a3c 100%)}
.search{left:407px;top:3px;width:145px;height:177px;background:var(--teal);padding:9px 12px;color:#fff}
.search h3{font-size:12px;font-weight:600;display:flex;align-items:center;gap:6px;padding-bottom:6px;border-bottom:1px solid rgba(255,255,255,.3);margin-bottom:8px}
.field{height:17px;background:#fff;border:1px solid #ccc;font-size:5.5px;color:#888;padding:4px 5px;margin-bottom:8px;position:relative}
.field.sel::after{content:"";position:absolute;right:5px;top:7px;border:2.5px solid transparent;border-top:3px solid #333}
.range{display:flex;align-items:flex-start;gap:5px;font-size:7px}
.range .field{width:50px}
.btn-search{height:17px;background:var(--red);color:#fff;font-family:"Exo",sans-serif;font-weight:600;font-size:8px;display:flex;align-items:center;justify-content:center}
.adv{text-align:right;font-size:5.5px;margin-top:4px}

/* reasons */
.block h2{font-size:10.5px;font-weight:600;color:#555;margin-bottom:8px}
.block p{font-size:6.5px;line-height:10.5px;color:var(--muted)}
.more{font-style:italic;text-decoration:underline;font-size:6.5px}
.more.g{color:var(--green)}
.more.r{color:var(--red)}
.reason{width:180px}
.reason .row{display:flex;gap:12px}
.reason svg{flex:none;width:24px;height:28px}

/* hot */
.hot-head{left:74px;top:530px;width:546px;height:24px;border-bottom:1px solid var(--line)}
.hot-head h2{font-size:11px;font-weight:700;color:#555;position:absolute;top:1px}
.tabs{left:143px;top:0;display:flex}
.tabs span{height:18px;padding:0 6px;font-size:6.5px;display:flex;align-items:center;border:1px solid #ccc;color:#999}
.tabs .on{background:var(--green);color:#fff;border-color:var(--green)}
.arrows{right:0;top:0;display:flex}
.arrows span{width:18px;height:18px;border:1px solid #ccc;color:#bbb;font-size:8px;display:flex;align-items:center;justify-content:center}
.card{top:565px;width:125px;height:170px;border:1px solid var(--line);box-shadow:0 1px 2px rgba(0,0,0,.08)}
.card .ph{height:93px}
.card h3{font-family:"Open Sans",sans-serif;font-weight:400;font-size:7.5px;color:var(--green);margin:8px 8px 1px}
.card .loc{font-size:6px;color:#666;margin:0 8px}
.feats{display:flex;gap:9px;margin:8px 8px;font-size:6px;color:#666;align-items:center}
.feats i{display:inline-block;width:12px;height:5px;background:var(--green);border-radius:2px;margin-left:3px;vertical-align:middle}
.price{position:absolute;left:0;right:0;bottom:0;height:23px;border-top:1px solid var(--line);display:flex;background:#fafafa}
.price b{flex:1;font-weight:400;color:var(--green);font-size:7.5px;display:flex;align-items:center;padding-left:8px}
.price span{width:45px;border-left:1px solid var(--line);display:flex;align-items:center;justify-content:center;font-size:6.5px;color:#555}

/* lower */
.col h2{font-size:11px;font-weight:600;color:#555}
.news{width:160px;font-size:6.5px;line-height:10.5px;color:#888}
.news .hl{color:var(--red)}
.news em{color:var(--red)}
.news hr{border:0;border-top:1px solid var(--line);margin:8px 0}
.viewall{font-style:italic;font-size:8px;color:#444}
.post{display:flex;gap:6px;margin-bottom:11px}
.thumb{width:58px;height:58px;border:1px solid #ddd;padding:4px;flex:none}
.thumb div{width:100%;height:100%}
.post p{font-size:7px;line-height:11px;color:#666;padding-top:6px}
.post small{display:flex;align-items:center;gap:5px;font-size:5px;color:#aaa;margin-top:6px}
.quote{width:178px;height:86px;border:1px solid #ccc;padding:10px 14px;font-size:7px;line-height:11.5px;color:#666;position:relative}
.quote::before{content:"\201C";position:absolute;left:4px;top:-2px;font-size:15px;color:#aaa}
.quote::after{content:"\201D";position:absolute;right:7px;bottom:-8px;font-size:15px;color:#aaa}
.who{display:flex;align-items:center;gap:6px;font-size:7.5px}
.avatar{width:36px;height:36px;border-radius:50%;background:linear-gradient(#6b4a30,#d9b89a)}

/* footer */
.footer{left:0;top:981px;width:698px;height:183px;background:var(--footer);color:#fff}
.footer h3{font-size:9.5px;font-weight:600;margin-bottom:11px}
.footer li{list-style:none;font-size:6.5px;line-height:14.6px}
.f-in{width:125px;height:15px;background:#fff;border:1px solid #aaa;font-size:5.5px;font-style:italic;color:#555;padding:3px 5px;margin-bottom:5px}
.f-in.big{height:31px}
.submit{width:50px;height:16px;background:var(--red);display:flex;align-items:center;justify-content:center;font-family:"Exo",sans-serif;font-size:8px;margin-top:5px}
.divider{left:216px;top:16px;width:1px;height:150px;background:#3a3a3a}
.copy{left:0;top:1164px;width:698px;height:36px;background:var(--footer-bar);color:#fff;font-size:6.5px;display:flex;align-items:center;justify-content:center}
</style>
</head>
<body>

<header>
  <div class="abs topband"></div>
  <div class="abs brand"><span class="brand-dot"></span><span class="brand-name">Juniper Estates</span></div>
  <div class="abs toplinks"><span>LOGIN</span><span>|</span><span>REGISTRATION</span><span>|</span><span>SITEMAP</span><span>|</span><span>HELP</span></div>
  <div class="abs pill" style="left:405px;width:143px">
    <svg width="9" height="7" viewBox="0 0 9 7"><rect x=".5" y=".5" width="8" height="6" fill="none" stroke="#fff"/><path d="M.5 .5 4.5 4 8.5 .5" fill="none" stroke="#fff"/></svg>info@juniper-estates.co.uk</div>
  <div class="abs pill" style="left:552px;width:80px">
    <svg width="5" height="9" viewBox="0 0 5 9"><rect x=".5" y=".5" width="4" height="8" rx="1" fill="none" stroke="#fff"/></svg>0700-5186420</div>
  <div class="abs login"><span>Email</span><span>Password</span><b>Login</b></div>
  <nav class="abs nav">
    <a style="width:89px">Home</a><a style="width:120px">Sell your property fast</a><a style="width:126px">Rent Your property fast</a><a style="width:99px">The 5 easy step</a><a style="width:64px">About</a><a style="width:57px">Contact</a>
  </nav>
</header>

<section class="abs hero">
  <div class="abs hero-photo" role="img" aria-label="Smiling couple standing beside a for sale sign in front of a yellow house"></div>
  <form class="abs search">
    <h3><svg width="10" height="10" viewBox="0 0 10 10"><circle cx="4" cy="4" r="3" fill="none" stroke="#fff" stroke-width="1.5"/><path d="M6 6 9.3 9.3" stroke="#fff" stroke-width="1.6"/></svg>Search</h3>
    <div class="field">Keyword</div>
    <div class="field sel">Select City</div>
    <div class="field sel">Property Type</div>
    <div class="range"><div class="field sel">$100</div><span style="padding-top:3px">To</span><div class="field sel">$1,300</div></div>
    <div class="btn-search">Search Property</div>
    <div class="adv">Advanced Search</div>
  </form>
</section>

<section>
  <div class="abs block" style="left:74px;top:348px;width:175px">
    <h2>Why Choose Us:</h2>
    <p>Lorem ipsum dolor sit amet, consectetur adipisicing elit, sed do eiusmod tempor incididunt ut labore et dolore magna aliqua.</p>
    <p style="margin-top:7px">sed do eiusmod tempor consectetur adipisicing elit, sed do eiusmod tempor incididunt ut labore et dolore magna aliqua.</p>
    <p style="margin-top:6px"><span class="more g">Read More</span></p>
  </div>

  <div class="abs block reason" style="left:263px;top:348px">
    <h2>Death</h2>
    <div class="row"><svg viewBox="0 0 24 28"><path d="M10 2h4v7h7v4h-7v9h5v4H5v-4h5v-9H3V9h7z" fill="var(--red)"/></svg>
    <p>Lorem ipsum dolor sit amet, consectetur adipisicing elit, sed do eiusmod tempor incididunt magna aliqua.<br><span class="more r">Read More</span></p></div>
  </div>
  <div class="abs block reason" style="left:451px;top:348px">
    <h2>Divorce/Separation</h2>
    <div class="row"><svg viewBox="0 0 24 28"><path d="M12 2 1 12h3v14h16V12h3z" fill="var(--red)"/><path d="M12 4 10 14l4 3-3 9" stroke="#fff" stroke-width="1.4" fill="none"/></svg>
    <p>Lorem ipsum dolor sit amet, consectetur adipisicing elit, sed do eiusmod tempor incididunt magna aliqua.<br><span class="more r">Read More</span></p></div>
  </div>
  <div class="abs block reason" style="left:263px;top:430px">
    <h2>Relocation</h2>
    <div class="row"><svg viewBox="0 0 24 28"><path d="M8 8a9 9 0 1 1 3 17l-2-3a6 6 0 1 0-2-11l3 3H1V5l3 3z" fill="var(--red)"/></svg>
    <p>Lorem ipsum dolor sit amet, consectetur adipisicing elit, sed do eiusmod tempor incididunt magna aliqua.<br><span class="more r">Read More</span></p></div>
  </div>
  <div class="abs block reason" style="left:451px;top:430px">
    <h2>Emigration</h2>
    <div class="row"><svg viewBox="0 0 24 28"><rect x="2" y="14" width="12" height="11" rx="1" fill="var(--red)"/><path d="M6 14v-3h4v3" stroke="var(--red)" stroke-width="2" fill="none"/><rect x="15" y="3" width="7" height="22" rx="1" fill="var(--red)"/></svg>
    <p>Lorem ipsum dolor sit amet, consectetur adipisicing elit, sed do eiusmod tempor incididunt magna aliqua.<br><span class="more r">Read More</span></p></div>
  </div>
</section>

<section>
  <div class="abs hot-head">
    <h2>HOT PROPERTIES</h2>
    <div class="abs tabs"><span class="on">For Rent</span><span>For Sale</span></div>
    <div class="abs arrows"><span>&#8249;</span><span>&#8250;</span></div>
  </div>

  <article class="abs card" style="left:75px">
    <div class="ph" role="img" aria-label="White villa with a swimming pool" style="background:linear-gradient(#5b8fc9,#e8e3d6 55%,#5ab7d8)"></div>
    <h3>6 Bedrooms Villa in Mirdif</h3><p class="loc">Mirdif City, Dubai</p>
    <div class="feats"><span>3<i></i></span><span>6<i></i></span><span>8<i></i></span></div>
    <div class="price"><b>AED 25,000</b><span>Details</span></div>
  </article>
  <article class="abs card" style="left:215px">
    <div class="ph" role="img" aria-label="City skyline of tall towers" style="background:linear-gradient(#9db6d6,#8a93a0 60%,#5d6670)"></div>
    <h3>2 Bedrooms Apartment</h3><p class="loc">Jabel Ali Residence, Dubai</p>
    <div class="feats"><span>3<i></i></span><span>6<i></i></span><span>8<i></i></span></div>
    <div class="price"><b>AED 66,000</b><span>Details</span></div>
  </article>
  <article class="abs card" style="left:355px">
    <div class="ph" role="img" aria-label="Waterfront hotel lit up at dusk" style="background:linear-gradient(#2e4f82,#4a6a9a 45%,#c59a52 80%,#3a3a48)"></div>
    <h3>2 Bedrooms Villa in Jumairah</h3><p class="loc">Jumairah, Dubai</p>
    <div class="feats"><span>3<i></i></span><span>6<i></i></span><span>8<i></i></span></div>
    <div class="price"><b>AED 125,000</b><span>Details</span></div>
  </article>
  <article class="abs card" style="left:495px">
    <div class="ph" role="img" aria-label="Family walking past sandy apartment buildings" style="background:linear-gradient(#c9b596,#a8896a 60%,#7a6a5e)"></div>
    <h3>4 Bedrooms Villa in Mirdif</h3><p class="loc">Mirdif City, Dubai</p>
    <div class="feats"><span>3<i></i></span><span>6<i></i></span><span>8<i></i></span></div>
    <div class="price"><b>AED 155,000</b><span>Details</span></div>
  </article>
</section>

<section>
  <div class="abs col" style="left:77px;top:766px">
    <h2>News and Events</h2>
    <div class="news" style="margin-top:18px">
      <p>Harlow Vale Marlborough Sauvignon <span class="hl">Blanced etc</span><br><em>posted on March 13, 2013 20:15</em></p>
      <p style="margin-top:6px">Media release; summer has never tasted better than with Harlow Vale's 2012 Sauvignon Blanc</p>
      <hr>
      <p>Harlow Vale Marlborough Sauvignon <span class="hl">Blanced etc</span><br><em>posted on March 13, 2013 20:15</em></p>
      <p style="margin-top:6px">Media release; summer has never tasted better than with Harlow Vale's 2012 Sauvignon Blanc</p>
    </div>
    <p class="viewall" style="margin-top:14px">View All</p>
  </div>

  <div class="abs col" style="left:259px;top:766px;width:170px">
    <h2>Our Blog</h2>
    <div style="margin-top:20px">
      <div class="post"><div class="thumb"><div role="img" aria-label="Rider on a motorbike mid jump" style="background:linear-gradient(#7fa8d8,#394a6a)"></div></div>
        <div><p>This in one of the important Blog Post of this website.</p><small><svg width="7" height="7"><rect x=".5" y="1" width="6" height="5.5" fill="none" stroke="#aaa"/></svg>25, JAN, 2011</small></div></div>
      <div class="post"><div class="thumb"><div role="img" aria-label="Child at a table" style="background:linear-gradient(#e8dccb,#b59a7a)"></div></div>
        <div><p>This in one of the important Blog Post of this website.</p><small><svg width="7" height="7"><rect x=".5" y="1" width="6" height="5.5" fill="none" stroke="#aaa"/></svg>25, JAN, 2011</small></div></div>
    </div>
    <p class="viewall" style="margin-top:2px;margin-left:3px">View All</p>
  </div>

  <div class="abs col" style="left:445px;top:766px">
    <h2>Testimonials</h2>
    <div class="quote" style="margin-top:16px">Lorem Ipsum is simply dummy text of the printing and typesetting industry. Lorem Ipsum has been the industry's standard dummy text ever since the 1500s, when</div>
    <div class="who" style="margin-top:6px;margin-left:2px"><div class="avatar" role="img" aria-label="Portrait of the customer"></div><div><span style="color:var(--red)">Maren Holt</span><br><span style="color:#666">Manager</span></div></div>
    <p class="viewall" style="margin-top:10px;margin-left:3px">View All</p>
  </div>
</section>

<footer class="abs footer">
  <div class="abs" style="left:75px;top:20px">
    <h3>Contact Us</h3>
    <div class="f-in">Enter your name...</div><div class="f-in">Enter your email</div><div class="f-in">Property Address</div><div class="f-in big">Enter your message</div>
    <div class="submit">Submit</div>
  </div>
  <div class="abs divider"></div>
  <div class="abs" style="left:240px;top:20px"><h3>Sitemap</h3><ul style="padding-left:2px"><li>Home</li><li>About Us</li><li>Rent</li><li>Sell</li><li>Special Offers</li><li>Easy 5 Steps</li><li>Contact Us</li></ul></div>
  <div class="abs" style="left:350px;top:20px"><h3>Products</h3><ul><li>Lorem Ipsum Dolor</li><li>Sit amet and Industry</li><li>That is all set</li><li>With this Type</li><li>And So On</li><li>With Lorem</li><li>And Ending</li></ul></div>
  <div class="abs" style="left:479px;top:20px;width:150px"><h3>Recent Posts</h3><p style="font-size:6.5px;line-height:14.6px">Lorem Ipsum is simply dummy text of the printing and typesetting industry. Lorem Ipsum has been the industry's standard dummy text ever since the 1500s, when an unknown printer took a galley of type and scrambled it to make a type specimen book.</p></div>
</footer>
<div class="abs copy">Copyright © 2013 Juniper Estates. All Rights Reserved</div>

</body>
</html>
```